Quran Index

hi im looking for someone to make a nice picture as psd file for the index of the quran complete in arabic and english all the words must be in text in psd file.

i have added a psd file i want the image done on top of the background i submited with the logo lunar vestokar showing and the arabic font on the top right corner also showing

the extra pictures i just added will give you a good idea how the theme colors of the app looks like, i dont want to be out of range, the colors of the quran index im looking for must match with the rest of the theme colors and feeling of the app..

thank you.

```html
<!DOCTYPE html>
<html lang="en">
<head>
<meta charset="utf-8">
<title>Quran Index</title>
<link rel="stylesheet" href="https://fonts.googleapis.com/css2?family=Amiri:wght@700&family=Tinos&display=swap">
<style>
  :root {
    --bg-deep: #0d4a6e;
    --bg-mid: #1a6a92;
    --bg-light: #2a82ab;
    --panel: rgba(120, 190, 225, 0.14);
    --rule: #b89a52;
    --text: #ffffff;
    --title-edge: #0a2f48;
    --ornament: #0b0f14;
  }
  * { margin: 0; padding: 0; box-sizing: border-box; }
  html, body { width: 1200px; height: 900px; overflow: hidden; }
  body { background: var(--bg-deep); }
  .canvas {
    position: relative;
    width: 1200px;
    height: 900px;
    overflow: hidden;
  }
  .backdrop {
    position: absolute; inset: 0;
    background: radial-gradient(ellipse at 50% 45%, var(--bg-light) 0%, var(--bg-mid) 45%, var(--bg-deep) 100%);
  }
  .corner {
    position: absolute;
    background: linear-gradient(135deg, var(--ornament), rgba(11, 15, 20, 0.55));
    opacity: 0.85;
  }
  .corner--top-right { top: 0; right: 0; width: 190px; height: 18px; }
  .corner--top-right-side { top: 0; right: 0; width: 18px; height: 440px; }
  .corner--bottom-left { bottom: 0; left: 0; width: 330px; height: 18px; }
  .corner--bottom-left-side { bottom: 0; left: 0; width: 18px; height: 440px; }
  .title {
    position: absolute;
    top: 38px; left: 0; right: 0;
    text-align: center;
    font-family: "Amiri", serif;
    font-weight: 700;
    font-size: 62px;
    color: var(--text);
    direction: rtl;
    -webkit-text-stroke: 3px var(--title-edge);
    paint-order: stroke fill;
  }
  .panel {
    position: absolute;
    left: 88px; top: 150px;
    width: 1092px; height: 712px;
    background: var(--panel);
  }
  .rule {
    position: absolute;
    top: 150px;
    width: 3px; height: 704px;
    border-left: 1px solid var(--rule);
    border-right: 1px solid var(--rule);
    opacity: 0.8;
  }
  .index-column {
    position: absolute;
    top: 154px;
    list-style: none;
    font-family: "Tinos", serif;
    font-size: 22.5px;
    color: var(--text);
  }
  .index-column li {
    display: flex;
    height: 30.5px;
    line-height: 30.5px;
    white-space: nowrap;
  }
  .surah-number {
    display: inline-block;
    text-align: right;
    margin-right: 9px;
  }
  .brand {
    position: absolute;
    right: 40px; bottom: 8px;
    font-family: "Tinos", serif;
    font-size: 28px;
    color: var(--text);
  }
</style>
</head>
<body>
<div class="canvas">
  <div class="backdrop" role="img" aria-label="Deep blue background with a faint repeating geometric pattern"></div>
  <div class="corner corner--top-right" role="img" aria-label="Black scrollwork border ornament"></div>
  <div class="corner corner--top-right-side" role="img" aria-label="Black scrollwork border ornament"></div>
  <div class="corner corner--bottom-left" role="img" aria-label="Black scrollwork border ornament"></div>
  <div class="corner corner--bottom-left-side" role="img" aria-label="Black scrollwork border ornament"></div>

  <h1 class="title">فهرس القرآن</h1>

  <div class="panel"></div>
  <div class="rule" style="left:276px"></div>
  <div class="rule" style="left:510px"></div>
  <div class="rule" style="left:726px"></div>
  <div class="rule" style="left:948px"></div>

  <ol class="index-column" style="left:88px">
    <li><span class="surah-number" style="width:32px">1</span>Al-Fatiha</li>
    <li><span class="surah-number" style="width:32px">2</span>Al-Baqara</li>
    <li><span class="surah-number" style="width:32px">3</span>Aal-E-Imran</li>
    <li><span class="surah-number" style="width:32px">4</span>An-Nisa</li>
    <li><span class="surah-number" style="width:32px">5</span>Al-Maeda</li>
    <li><span class="surah-number" style="width:32px">6</span>Al-Anaam</li>
    <li><span class="surah-number" style="width:32px">7</span>Al-Araf</li>
    <li><span class="surah-number" style="width:32px">8</span>Al-Anfal</li>
    <li><span class="surah-number" style="width:32px">9</span>At-Tawba</li>
    <li><span class="surah-number" style="width:32px">10</span>Yunus</li>
    <li><span class="surah-number" style="width:32px">11</span>Hud</li>
    <li><span class="surah-number" style="width:32px">12</span>Yusuf</li>
    <li><span class="surah-number" style="width:32px">13</span>Ar-Rad</li>
    <li><span class="surah-number" style="width:32px">14</span>Ibrahim</li>
    <li><span class="surah-number" style="width:32px">15</span>Al-Hijr</li>
    <li><span class="surah-number" style="width:32px">16</span>An-Nahl</li>
    <li><span class="surah-number" style="width:32px">17</span>Al-Isra</li>
    <li><span class="surah-number" style="width:32px">18</span>Al-Kahf</li>
    <li><span class="surah-number" style="width:32px">19</span>Maryam</li>
    <li><span class="surah-number" style="width:32px">20</span>Ta-Ha</li>
    <li><span class="surah-number" style="width:32px">21</span>Al-Anbiya</li>
    <li><span class="surah-number" style="width:32px">22</span>Al-Hajj</li>
    <li><span class="surah-number" style="width:32px">23</span>Al-Mumenoon</li>
  </ol>

  <ol class="index-column" style="left:318px">
    <li><span class="surah-number" style="width:30px">24</span>An-Noor</li>
    <li><span class="surah-number" style="width:30px">25</span>Al-Furqan</li>
    <li><span class="surah-number" style="width:30px">26</span>Ash-Shuara</li>
    <li><span class="surah-number" style="width:30px">27</span>An-Naml</li>
    <li><span class="surah-number" style="width:30px">28</span>Al-Qasas</li>
    <li><span class="surah-number" style="width:30px">29</span>Al-Ankaboot</li>
    <li><span class="surah-number" style="width:30px">30</span>Ar-Room</li>
    <li><span class="surah-number" style="width:30px">31</span>Luqman</li>
    <li><span class="surah-number" style="width:30px">32</span>As-Sajda</li>
    <li><span class="surah-number" style="width:30px">33</span>Al-Ahzab</li>
    <li><span class="surah-number" style="width:30px">34</span>Saba</li>
    <li><span class="surah-number" style="width:30px">35</span>Surat Fatir</li>
    <li><span class="surah-number" style="width:30px">36</span>Ya-Seen</li>
    <li><span class="surah-number" style="width:30px">37</span>As-Saaffat</li>
    <li><span class="surah-number" style="width:30px">38</span>Sad</li>
    <li><span class="surah-number" style="width:30px">39</span>Az-Zumar</li>
    <li><span class="surah-number" style="width:30px">40</span>Ghafir</li>
    <li><span class="surah-number" style="width:30px">41</span>Fussilat</li>
    <li><span class="surah-number" style="width:30px">42</span>Ash-Shura</li>
    <li><span class="surah-number" style="width:30px">43</span>Az-Zukhruf</li>
    <li><span class="surah-number" style="width:30px">44</span>Ad-Dukhan</li>
    <li><span class="surah-number" style="width:30px">45</span>Al-Jathiya</li>
    <li><span class="surah-number" style="width:30px">46</span>Al-Ahqaf</li>
  </ol>

  <ol class="index-column" style="left:522px">
    <li><span class="surah-number" style="width:30px">47</span>Muhammad</li>
    <li><span class="surah-number" style="width:30px">48</span>Al-Fath</li>
    <li><span class="surah-number" style="width:30px">49</span>Al-Hujraat</li>
    <li><span class="surah-number" style="width:30px">50</span>Qaf</li>
    <li><span class="surah-number" style="width:30px">51</span>Adh-Dhariyat</li>
    <li><span class="surah-number" style="width:30px">52</span>At-Tur</li>
    <li><span class="surah-number" style="width:30px">53</span>An-Najm</li>
    <li><span class="surah-number" style="width:30px">54</span>Al-Qamar</li>
    <li><span class="surah-number" style="width:30px">55</span>Ar-Rahman</li>
    <li><span class="surah-number" style="width:30px">56</span>Al-Waqia</li>
    <li><span class="surah-number" style="width:30px">57</span>Al-Hadid</li>
    <li><span class="surah-number" style="width:30px">58</span>Al-Mujadila</li>
    <li><span class="surah-number" style="width:30px">59</span>Al-Hashr</li>
    <li><span class="surah-number" style="width:30px">60</span>Al-Mumtahina</li>
    <li><span class="surah-number" style="width:30px">61</span>As-Saff</li>
    <li><span class="surah-number" style="width:30px">62</span>Al-Jumua</li>
    <li><span class="surah-number" style="width:30px">63</span>Al-Munafiqoon</li>
    <li><span class="surah-number" style="width:30px">64</span>At-Taghabun</li>
    <li><span class="surah-number" style="width:30px">65</span>At-Talaq</li>
    <li><span class="surah-number" style="width:30px">66</span>At-Tahrim</li>
    <li><span class="surah-number" style="width:30px">67</span>Al-Mulk</li>
    <li><span class="surah-number" style="width:30px">68</span>Al-Qalam</li>
    <li><span class="surah-number" style="width:30px">69</span>Al-Haaqqa</li>
  </ol>

  <ol class="index-column" style="left:756px">
    <li><span class="surah-number" style="width:30px">70</span>Al-Maarij</li>
    <li><span class="surah-number" style="width:30px">71</span>Nooh</li>
    <li><span class="surah-number" style="width:30px">72</span>Al-Jinn</li>
    <li><span class="surah-number" style="width:30px">73</span>Al-Muzzammil</li>
    <li><span class="surah-number" style="width:30px">74</span>Al-Muddaththir</li>
    <li><span class="surah-number" style="width:30px">75</span>Al-Qiyama</li>
    <li><span class="surah-number" style="width:30px">76</span>Al-Insan</li>
    <li><span class="surah-number" style="width:30px">77</span>Al-Mursalat</li>
    <li><span class="surah-number" style="width:30px">78</span>An-Naba</li>
    <li><span class="surah-number" style="width:30px">79</span>An-Naziat</li>
    <li><span class="surah-number" style="width:30px">80</span>Abasa</li>
    <li><span class="surah-number" style="width:30px">81</span>At-Takwir</li>
    <li><span class="surah-number" style="width:30px">82</span>Al-Infitar</li>
    <li><span class="surah-number" style="width:30px">83</span>Al-Mutaffifin</li>
    <li><span class="surah-number" style="width:30px">84</span>Al-Inshiqaq</li>
    <li><span class="surah-number" style="width:30px">85</span>Al-Burooj</li>
    <li><span class="surah-number" style="width:30px">86</span>At-Tariq</li>
    <li><span class="surah-number" style="width:30px">87</span>Al-Ala</li>
    <li><span class="surah-number" style="width:30px">88</span>Al-Ghashiya</li>
    <li><span class="surah-number" style="width:30px">89</span>Al-Fajr</li>
    <li><span class="surah-number" style="width:30px">90</span>Al-Balad</li>
    <li><span class="surah-number" style="width:30px">91</span>Ash-Shams</li>
    <li><span class="surah-number" style="width:30px">92</span>Al-Lail</li>
  </ol>

  <ol class="index-column" style="left:942px">
    <li><span class="surah-number" style="width:44px">93</span>Ad-Dhuha</li>
    <li><span class="surah-number" style="width:44px">94</span>Al-Inshirah</li>
    <li><span class="surah-number" style="width:44px">95</span>At-Tin</li>
    <li><span class="surah-number" style="width:44px">96</span>Al-Alaq</li>
    <li><span class="surah-number" style="width:44px">97</span>Al-Qadr</li>
    <li><span class="surah-number" style="width:44px">98</span>Al-Bayyina</li>
    <li><span class="surah-number" style="width:44px">99</span>Az-Zalzala</li>
    <li><span class="surah-number" style="width:44px">100</span>Al-Adiyat</li>
    <li><span class="surah-number" style="width:44px">101</span>Al-Qaria</li>
    <li><span class="surah-number" style="width:44px">102</span>At-Takathur</li>
    <li><span class="surah-number" style="width:44px">103</span>Al-Asr</li>
    <li><span class="surah-number" style="width:44px">104</span>Al-Humaza</li>
    <li><span class="surah-number" style="width:44px">105</span>Al-Fil</li>
    <li><span class="surah-number" style="width:44px">106</span>Quraish</li>
    <li><span class="surah-number" style="width:44px">107</span>Al-Maun</li>
    <li><span class="surah-number" style="width:44px">108</span>Al-Kauther</li>
    <li><span class="surah-number" style="width:44px">109</span>Al-Kafiroon</li>
    <li><span class="surah-number" style="width:44px">110</span>An-Nasr</li>
    <li><span class="surah-number" style="width:44px">111</span>Al-Masadd</li>
    <li><span class="surah-number" style="width:44px">112</span>Al-Ikhlas</li>
    <li><span class="surah-number" style="width:44px">113</span>Al-Falaq</li>
    <li><span class="surah-number" style="width:44px">114</span>An-Nas</li>
  </ol>

  <div class="brand">Lunar Vestokar</div>
</div>
</body>
</html>
```